Unique and original Business Card for Financial Services Business

I have moved premises and need to change the detail on my business card so thought now is a good time for a re-design. Looking for something professional and modern with colours to fit in with out logo. Like the idea of foil or embossing if that works but not a must have but I do want something that stands out and that I could not design myself.

Once business card is designed I will also be looking to get letterhead and flyers done but want the business card concept in place first.

The majority of designs I am receiving are generic and template based. I am looking for something unique and original. We have some great design elements in our logo, think outside the box and show me something that stands out from the crowd.

Target Market(s)

Business Professionals

Industry/Entity Type

Finance

Contact Information for Business Card

Name: Delphine Moore Phone 0438 297 614 Address PO Box 7816 Ashvale NSW 2411 Email info@tidewellmoneyservices.example.com.au website www.tidewellmoneyservices.example.com.au

Font styles to use
Other font styles liked:
• Ralway

Requirements
Should not have
• No black backgrounds please

```html
<!DOCTYPE html>
<html lang="en">
<head>
<meta charset="utf-8">
<title>Tidewell Money Services – Business Card</title>
<link href="https://fonts.googleapis.com/css2?family=Urbanist:wght@400;500;700;800&display=swap" rel="stylesheet">
<style>
  :root {
    --backdrop: #8f9090;
    --card-white: #ecedef;
    --teal-deep: #0b5f70;
    --teal-card: #007b8c;
    --teal-light: #14a3b3;
    --ink: #1c1c1e;
  }
  * { margin: 0; padding: 0; box-sizing: border-box; }
  html, body { width: 1200px; height: 1200px; overflow: hidden; }
  body {
    background: var(--backdrop);
    font-family: "Urbanist", "Helvetica Neue", Arial, sans-serif;
    position: relative;
  }
  .card {
    position: absolute;
    width: 750px;
    height: 415px;
  }
  .card-front { left: 233px; top: 101px; background: var(--card-white); }
  .card-back  { left: 231px; top: 668px; background: var(--teal-card); }

  .holder { position: absolute; left: 52px; top: 56px; }
  .holder-name {
    font-size: 28px; font-weight: 800; color: var(--teal-deep);
    letter-spacing: 0.2px; line-height: 1;
  }
  .holder-role {
    margin-top: 5px; font-size: 20px; font-weight: 500; color: var(--ink); line-height: 1;
  }

  .brand-front {
    position: absolute; right: 52px; top: 92px;
    display: flex; align-items: center; gap: 16px;
  }
  .brand-mark {
    width: 58px; height: 58px; border-radius: 50%; background: var(--teal-deep); flex: none;
  }
  .brand-name {
    font-size: 30px; font-weight: 700; color: var(--teal-deep); line-height: 1.1;
  }

  .contact-list {
    position: absolute; left: 52px; top: 246px; list-style: none;
  }
  .contact-list li {
    display: flex; align-items: center; gap: 9px;
    height: 29px; font-size: 20px; font-weight: 500; color: var(--ink);
  }
  .contact-icon { width: 22px; height: 22px; flex: none; }

  .brand-back {
    position: absolute; left: 0; right: 0; top: 150px;
    display: flex; flex-direction: column; align-items: center; gap: 22px;
  }
  .brand-back .brand-mark {
    width: 96px; height: 96px; background: var(--teal-light);
  }
  .brand-back .brand-name {
    color: var(--teal-light); font-size: 46px; font-weight: 500;
  }
</style>
</head>
<body>

<section class="card card-front">
  <div class="holder">
    <p class="holder-name">Delphine Moore</p>
    <p class="holder-role">Owner</p>
  </div>

  <div class="brand-front">
    <span class="brand-mark"></span>
    <p class="brand-name">Tidewell<br>Money Services</p>
  </div>

  <ul class="contact-list">
    <li>
      <svg class="contact-icon" viewBox="0 0 24 24"><circle cx="12" cy="12" r="12" fill="#0b5f70"/><path d="M8.2 6.5l1.9-.4 1.2 3-1.3 1c.6 1.4 1.6 2.5 3 3.1l1-1.3 3 1.2-.4 1.9c-.2.6-.8 1-1.5.9-4-.6-7.2-3.8-7.8-7.8-.1-.7.3-1.4.9-1.6z" fill="#fff"/></svg>
      <span>0438 297 614</span>
    </li>
    <li>
      <svg class="contact-icon" viewBox="0 0 24 24"><circle cx="12" cy="12" r="12" fill="#0b5f70"/><path d="M12 4.5c-3 0-5.2 2.3-5.2 5.1 0 3.6 5.2 9.2 5.2 9.2s5.2-5.6 5.2-9.2c0-2.8-2.2-5.1-5.2-5.1z" fill="#fff"/><circle cx="12" cy="9.7" r="2" fill="#0b5f70"/></svg>
      <span>PO Box 7816 Ashvale NSW 2411</span>
    </li>
    <li>
      <svg class="contact-icon" viewBox="0 0 24 24"><circle cx="12" cy="12" r="12" fill="#0b5f70"/><rect x="6" y="7.5" width="12" height="9" rx="1.5" fill="#fff"/><path d="M6.8 8.5l5.2 4 5.2-4" stroke="#0b5f70" stroke-width="1.4" fill="none"/></svg>
      <span>info@tidewellmoneyservices.example.com.au</span>
    </li>
    <li>
      <svg class="contact-icon" viewBox="0 0 24 24"><circle cx="12" cy="12" r="12" fill="#0b5f70"/><g stroke="#fff" stroke-width="1.3" fill="none"><circle cx="12" cy="12" r="6"/><ellipse cx="12" cy="12" rx="2.6" ry="6"/><path d="M6 12h12"/></g></svg>
      <span>www.tidewellmoneyservices.example.com.au</span>
    </li>
  </ul>
</section>

<section class="card card-back">
  <div class="brand-back">
    <span class="brand-mark"></span>
    <p class="brand-name">Tidewell Money Services</p>
  </div>
</section>

</body>
</html>
```